BC Postcard # 1

Front:
Please design a 4-color, 2 sided postcard with the following information:

Headline: 5 Million Seniors in the U.S. Suffer with Alzheimer's or a Related Dementia!

2nd Headline: Is your organization ready to meet the challenge?

Back (postage and address side):

Brightpath Cognitive LLC
PO Box 437
Fernhollow, NY 12873

Call to action:

Call Today
For a FREE Price Quote!
845-317-2264
or go online to:
www.brightpathcognitive.com/ready
(Choose from Several Plans)

This is what we do:
We train healthcare professionals in best-care practices for people with memory impairment. We help hospitals, assisted livings, nursing homes, and home care agencies to become dementia-ready.

The postcard should use the colors in the logo and any other graphics you select.

```html
<!DOCTYPE html>
<html lang="en">
<head>
<meta charset="utf-8">
<title>Brightpath Cognitive Postcard</title>
<link rel="stylesheet" href="https://fonts.googleapis.com/css2?family=Arimo:wght@400;700&family=Open+Sans:wght@300&display=swap">
<style>
  :root {
    --navy: #3b4a7e;
    --green: #8fac4a;
    --sky: #1a9ad6;
    --band: rgba(46, 150, 205, 0.82);
    --paper: #ffffff;
    --logo-bg: #f6f5f8;
    --logo-ink: #5a5670;
    --rule: #9a9a9a;
  }
  * { box-sizing: border-box; margin: 0; padding: 0; }
  html, body { width: 920px; height: 1200px; overflow: hidden; background: var(--paper); }
  body { position: relative; font-family: "Arimo", Arial, sans-serif; }

  .card { position: absolute; left: 31px; width: 858px; border: 1px solid #b8b8b8; overflow: hidden; background: var(--paper); }
  .card--front { top: 29px; height: 552px; }
  .card--back { top: 619px; height: 554px; }

  /* Front */
  .front__topbar { position: absolute; left: 0; top: 0; width: 446px; height: 49px; background: var(--navy); }
  .front__logo-box { position: absolute; left: 0; top: 49px; width: 389px; height: 154px; background: var(--logo-bg);
    display: flex; align-items: center; padding-left: 40px; }
  .brand-name { font-family: "Arimo", Arial, sans-serif; font-weight: 400; font-size: 25px; color: var(--logo-ink); line-height: 1.2; }
  .front__logo-accent { position: absolute; left: 389px; top: 49px; width: 57px; height: 154px; background: var(--green); }
  .front__panel { position: absolute; left: 0; top: 203px; width: 446px; height: 349px; background: var(--navy); }
  .headline { position: absolute; left: 36px; top: 219px; width: 400px; color: #fff; font-weight: 400;
    font-size: 40px; line-height: 56px; letter-spacing: -0.3px; }
  .front__photo { position: absolute; left: 446px; top: 0; width: 412px; height: 552px;
    background: linear-gradient(160deg, #f2efec 0%, #dfe6ea 30%, #2b9fd0 55%, #e9e4f0 72%, #8fbf6a 100%); }
  .subhead-bar { position: absolute; left: 0; top: 456px; width: 858px; height: 55px; }
  .subhead-bar__mark { position: absolute; left: 0; top: 0; width: 35px; height: 55px; background: var(--green); }
  .subhead-bar__band { position: absolute; left: 35px; top: 0; width: 791px; height: 55px; background: var(--band); }
  .subhead-bar__end { position: absolute; left: 826px; top: 0; width: 32px; height: 55px; background: var(--navy); }
  .subhead { position: absolute; left: 44px; top: 6px; font-family: "Open Sans", Arial, sans-serif; font-weight: 300;
    font-size: 34px; letter-spacing: -1.2px; color: #fff; white-space: nowrap; line-height: 42px; }

  /* Back */
  .back__about { position: absolute; left: 0; top: 0; width: 438px; height: 198px; background: var(--sky);
    padding: 40px 32px 0 53px; }
  .about-text { color: #fff; font-size: 15.5px; line-height: 24.5px; text-align: justify; }
  .back__contact { position: absolute; left: 0; top: 198px; width: 438px; height: 356px; background: var(--navy); }
  .back__contact-accent { position: absolute; left: 0; top: 32px; width: 35px; height: 324px; background: var(--green); }
  .contact { position: absolute; left: 53px; top: 32px; color: #fff; font-weight: 700; font-size: 18px; line-height: 23.5px; }
  .contact p + p { margin-top: 23.5px; }
  .back__mail { position: absolute; left: 438px; top: 0; width: 420px; height: 554px; }
  .stamp-box { position: absolute; left: 269px; top: 36px; width: 98px; height: 128px; border: 1px solid #555; }
  .address-line { position: absolute; left: 86px; width: 312px; height: 0; border-top: 1px solid var(--rule); }
</style>
</head>
<body>
  <section class="card card--front" aria-label="Postcard front">
    <div class="front__topbar"></div>
    <div class="front__logo-box"><span class="brand-name">Brightpath Cognitive LLC</span></div>
    <div class="front__logo-accent"></div>
    <div class="front__panel"></div>
    <h1 class="headline">5 Million Seniors in the U.S. Suffer with Alzheimer's or a Related Dementia!</h1>
    <div class="front__photo" role="img" aria-label="Photo of a smiling nurse in blue scrubs comforting an elderly woman resting in bed"></div>
    <div class="subhead-bar">
      <div class="subhead-bar__mark"></div>
      <div class="subhead-bar__band"></div>
      <div class="subhead-bar__end"></div>
      <h2 class="subhead">Is your organization ready to meet the challenge?</h2>
    </div>
  </section>

  <section class="card card--back" aria-label="Postcard back">
    <div class="back__about">
      <p class="about-text">We train healthcare professionals in best-care practices for people with memory impairment. We help hospitals, assisted livings, nursing homes, and home care agencies to become dementia-ready.</p>
    </div>
    <div class="back__contact">
      <div class="back__contact-accent"></div>
      <div class="contact">
        <p>Brightpath Cognitive LLC<br>PO Box 437<br>Fernhollow, NY 12873</p>
        <p>Call to action:</p>
        <p>Call Today<br>For a FREE Price Quote!<br>845-317-2264<br>or go online to:<br>www.brightpathcognitive.com<br>(Choose from Several Plans)</p>
      </div>
    </div>
    <div class="back__mail">
      <div class="stamp-box"></div>
      <div class="address-line" style="top:222px"></div>
      <div class="address-line" style="top:275px"></div>
      <div class="address-line" style="top:326px"></div>
      <div class="address-line" style="top:379px"></div>
    </div>
  </section>
</body>
</html>
```